New Office Poster Designs

Attached you will find 3 poster designs that we found online along with our logos. Please use our logos to reference any type of color or design.
These posters will be hung around our Loan Offices.

INSTRUCTIONS: Please mimic all 3 posters (MINUS THE SMALL WRITING ON THEM THAT IS NOT IN ENGLISH IGNORE THAT)
but use our logos and colors. Also, if you can make them in Spanish as well as English that is a plus. We will also need 1 additional poster with the below wording.

Additional Poster:
Stuck in a Title Loan? Let us pay it off up to $10,000

Target Market(s)

People looking to get a loan and need money

Industry/Entity Type

Loan Industry - Consumer Lending - Fast easy loans

Requirements
Nice to have
• English and Spanish

```html
<!DOCTYPE html>
<html lang="en">
<head>
<meta charset="utf-8">
<title>Title Loan Payoff Posters – English and Spanish</title>
<link rel="stylesheet" href="https://fonts.googleapis.com/css2?family=Poppins:wght@300;400;600;700&display=swap">
<style>
  :root {
    --backdrop: #e4e4e4;
    --paper: #ffffff;
    --loan-red: #c11f29;
    --loan-red-deep: #a8161f;
    --loan-red-light: #cf2a33;
    --loan-green: #0e5a2f;
    --ink-white: #ffffff;
    --divider: rgba(255, 255, 255, 0.55);
  }
  * { margin: 0; padding: 0; box-sizing: border-box; }
  html, body {
    width: 1200px;
    height: 885px;
    overflow: hidden;
    background: var(--backdrop);
    font-family: "Poppins", sans-serif;
    color: var(--ink-white);
  }
  .poster {
    position: absolute;
    top: 159px;
    width: 410px;
    height: 574px;
    background: var(--paper);
  }
  .poster--english { left: 134px; }
  .poster--spanish { left: 664px; }

  .sheet {
    position: absolute;
    inset: 8px 8px 8px 8px;
    background: var(--loan-red);
    overflow: hidden;
  }
  .money-texture {
    position: absolute;
    inset: 0;
    background:
      radial-gradient(ellipse at 20% 15%, var(--loan-red-light) 0%, transparent 45%),
      radial-gradient(ellipse at 80% 70%, var(--loan-red-light) 0%, transparent 50%),
      linear-gradient(160deg, var(--loan-red) 0%, var(--loan-red-deep) 100%);
  }
  .inner-frame {
    position: absolute;
    left: 12px;
    right: 11px;
    top: 11px;
    height: 418px;
    border: 1px solid var(--ink-white);
    border-bottom: none;
  }
  .brand-box {
    position: absolute;
    left: 124px;
    top: 11px;
    width: 147px;
    height: 87px;
    background: var(--paper);
    display: flex;
    align-items: center;
    justify-content: center;
    text-align: center;
  }
  .brand-name {
    color: var(--loan-green);
    font-weight: 600;
    font-size: 19px;
    line-height: 1.15;
  }
  .line {
    position: absolute;
    left: 0;
    width: 100%;
    text-align: center;
    line-height: 1;
    white-space: nowrap;
  }
  .line--light { font-weight: 300; }
  .line--bold { font-weight: 700; }
  .divider {
    position: absolute;
    height: 1px;
    background: var(--divider);
  }
  .amount {
    position: absolute;
    left: 0;
    width: 100%;
    display: flex;
    justify-content: center;
    align-items: center;
    gap: 6px;
  }
  .amount-prefix {
    writing-mode: vertical-rl;
    transform: rotate(180deg);
    font-weight: 400;
    font-size: 13px;
    letter-spacing: 0.5px;
  }
  .amount-value {
    font-weight: 700;
    font-size: 58px;
    line-height: 1;
  }
  .contact-band {
    position: absolute;
    left: 12px;
    top: 428px;
    width: 371px;
    height: 118px;
    background: var(--loan-green);
    padding: 14px 35px 0 35px;
  }
  .contact-row {
    display: flex;
    justify-content: space-between;
    align-items: baseline;
  }
  .offer-label { font-weight: 400; font-size: 19px; }
  .offer-label--es { font-size: 16px; }
  .phone { font-weight: 700; font-size: 22px; letter-spacing: 0.3px; }
  .web-row {
    display: flex;
    align-items: center;
    gap: 6px;
    margin-top: 4px;
    font-size: 11.5px;
  }
  .web-row strong { font-weight: 700; }
  .web-rule { flex: 1; height: 1px; background: var(--ink-white); }
  .fine-print {
    margin-top: 8px;
    font-size: 5.3px;
    line-height: 1.4;
    text-align: justify;
  }
</style>
</head>
<body>

<section class="poster poster--english" lang="en">
  <div class="sheet">
    <div class="money-texture" role="img" aria-label="Red-tinted background of scattered dollar bills"></div>
    <div class="inner-frame"></div>
    <div class="brand-box"><span class="brand-name">Crestline<br>Loans</span></div>

    <p class="line line--light" style="top:146px;font-size:47px;">STUCK IN A</p>
    <p class="line line--bold" style="top:196px;font-size:50px;">TITLE LOAN?</p>
    <div class="divider" style="top:266px;left:53px;width:288px;"></div>
    <p class="line line--light" style="top:286px;font-size:33px;">LET US PAY IT OFF</p>
    <div class="amount" style="top:323px;">
      <span class="amount-prefix">UP TO</span>
      <span class="amount-value">$10,000</span>
    </div>

    <div class="contact-band">
      <div class="contact-row">
        <span class="offer-label">Limited time</span>
        <span class="phone">0123-456-789</span>
      </div>
      <div class="web-row"><span>www.<strong>crestlineloans</strong>.com</span><span class="web-rule"></span></div>
      <p class="fine-print">Offer available for qualifying vehicle title loans only. Approval depends on verification of income, identity and current loan balance. Payoff amount is sent directly to your existing lender. Terms, rates and fees vary by state and applicant. Visit any of our offices or call today to speak with a friendly loan specialist about your options.</p>
    </div>
  </div>
</section>

<section class="poster poster--spanish" lang="es">
  <div class="sheet">
    <div class="money-texture" role="img" aria-label="Fondo rojo de billetes de dólar dispersos"></div>
    <div class="inner-frame"></div>
    <div class="brand-box"><span class="brand-name">Crestline<br>Loans</span></div>

    <p class="line line--light" style="top:136px;font-size:30px;">ATRAPADO EN UN</p>
    <p class="line line--bold" style="top:168px;font-size:52px;">PRÉSTAMO</p>
    <p class="line line--bold" style="top:219px;font-size:52px;">DE TÍTULO?</p>
    <div class="divider" style="top:286px;left:53px;width:288px;"></div>
    <p class="line line--light" style="top:300px;font-size:31px;">VAMOS A PAGARLO</p>
    <div class="amount" style="top:332px;">
      <span class="amount-prefix">HASTA</span>
      <span class="amount-value">$10,000</span>
    </div>

    <div class="contact-band">
      <div class="contact-row">
        <span class="offer-label offer-label--es">Tiempo limitado</span>
        <span class="phone">0123-456-789</span>
      </div>
      <div class="web-row"><span>www.<strong>crestlineloans</strong>.com</span><span class="web-rule"></span></div>
      <p class="fine-print" lang="en">Offer available for qualifying vehicle title loans only. Approval depends on verification of income, identity and current loan balance. Payoff amount is sent directly to your existing lender. Terms, rates and fees vary by state and applicant. Visit any of our offices or call today to speak with a friendly loan specialist about your options.</p>
    </div>
  </div>
</section>

</body>
</html>
```